Veterinary TPLO Surgery Flyer Design

Please use this flyer to make a professional-looking 1 page, double-sided client handout regarding TPLO.

You can visit our website at www.brookferrypetcare.com & www.northgroveanimalsurgery.com for additional logo information. The flyer should include all the text from the one provided.

Target Market(s)

Client communication to for referral surgery between sister veterinary clinics

Industry/Entity Type

Veterinary

Requirements
Must have
• The text included
Nice to have
• Nice to have the Willow Crest Avenue Animal CLinic & Dr. Pettigrew Mobile vet logos incorporated.

```html
<!DOCTYPE html>
<html lang="en">
<head>
<meta charset="utf-8">
<title>TPLO Surgery Client Handout</title>
<link rel="stylesheet" href="https://fonts.googleapis.com/css2?family=Tinos:wght@400;700&display=swap">
<style>
  :root {
    --green: #26845b;
    --green-deep: #0d6a3c;
    --yellow: #ffec00;
    --white: #ffffff;
    --ink: #1d3a2a;
    --backdrop: #e9ebea;
    --serif: "Tinos", "Times New Roman", serif;
  }
  * { box-sizing: border-box; margin: 0; padding: 0; }
  html, body { width: 1200px; height: 1200px; overflow: hidden; background: var(--backdrop); }
  .spread { position: relative; width: 1200px; height: 1200px; }
  .page {
    position: absolute; top: 203px; width: 560px; height: 793px; overflow: hidden;
    font-family: var(--serif); color: var(--white);
  }
  .page--back { left: 30px; background: var(--green-deep); }
  .page--front { left: 610px; background: var(--white); }

  .back-photo {
    position: absolute; inset: 0;
    background:
      radial-gradient(ellipse 40% 45% at 62% 52%, rgba(120,150,60,.45), transparent 70%),
      linear-gradient(160deg, #2f8a5c 0%, #1f7a4b 45%, #0b5f33 100%);
  }
  .body-text { font-size: 7.9px; line-height: 10.2px; }
  .body-text b { font-weight: 700; }
  .back-copy { position: absolute; left: 34px; top: 44px; width: 490px; }

  .specialist-panel {
    position: absolute; left: 168px; top: 397px; width: 225px; height: 225px;
    background: var(--white); display: flex; align-items: center; justify-content: center;
  }
  .specialist-name { font-family: var(--serif); font-weight: 700; font-size: 24px; color: var(--green-deep); text-align: center; line-height: 1.15; }
  .clinic-name {
    position: absolute; display: flex; align-items: center; gap: 8px;
    font-family: var(--serif); font-weight: 700; color: var(--white); line-height: 1.1;
  }
  .clinic-name .mark { width: 12px; height: 12px; background: var(--yellow); flex: none; }
  .clinic-name--back { left: 168px; top: 642px; width: 240px; font-size: 17px; }

  .front-field { position: absolute; inset: 0; }
  .clinic-name--front { left: 34px; top: 46px; width: 170px; font-size: 12px; color: var(--green-deep); }
  .clinic-name--front .mark { width: 10px; height: 10px; background: var(--green); }
  .specialist-name--front { position: absolute; left: 34px; top: 92px; width: 110px; font-size: 12px; color: var(--green-deep); text-align: left; }

  .photo-ring {
    position: absolute; border-radius: 50%; border: 14px solid var(--yellow);
    width: 258px; height: 258px;
  }
  .photo-ring--cat { left: 266px; top: 36px;
    background: radial-gradient(circle at 50% 55%, #d9873a 0%, #c47735 35%, #e9e4dc 70%, #f3f1ee 100%); }
  .photo-ring--pups { left: 34px; top: 196px;
    background: radial-gradient(circle at 50% 55%, #d7a466 0%, #c48c4d 40%, #7f9a4a 75%, #6d8a3d 100%); }

  .front-copy { position: absolute; left: 34px; top: 464px; width: 492px; }

  .contacts { position: absolute; left: 34px; top: 698px; width: 500px; display: flex; font-size: 7.9px; line-height: 10.2px; }
  .contact-block { padding-left: 12px; }
  .contact-block--clinic { width: 172px; }
  .contact-block--surgeon { border-left: 1px solid var(--yellow); margin-top: 6px; padding-left: 18px; }
  .contact-title { font-weight: 700; margin-bottom: 7px; margin-left: 12px; }
  .contact-block--surgeon .contact-title { margin-left: -4px; margin-top: -4px; }
  .contact-line { display: flex; align-items: flex-start; gap: 4px; }
  .contact-line svg { width: 8px; height: 8px; margin-top: 1px; flex: none; }
</style>
</head>
<body>
<div class="spread">

  <section class="page page--back">
    <div class="back-photo" role="img" aria-label="Faded photograph of a tabby cat sitting indoors, tinted green"></div>
    <div class="back-copy body-text">
      <p><b>Diagnostic Radiographs vs. TPLO Planning Radiographs</b> While diagnostic radiographs may confirm a CCL tear, they are not sufficient for surgical planning. TPLO requires three advanced technique radiographic views with precise measurements, which must be performed under sedation to reduce discomfort and allow accurate positioning.</p>
      <p><b>Expected Process</b></p>
      <p>1. <b>Diagnosis:</b> Your pet is diagnosed with stifle instability (CCL tear) by your veterinarian.</p>
      <p>2. <b>Referral:</b> Your veterinarian contacts the surgical coordinator at Willow Crest Avenue Animal Clinic.</p>
      <p>3. <b>Consultation:</b> The coordinator contacts you to schedule a 1-hour consultation to review the procedure, estimated costs, and available surgery dates.</p>
      <p>4. <b>Planning Radiographs:</b> These specialized X-rays are typically taken during the consultation under light sedation.</p>
      <p>5. <b>Surgical Review:</b> Dr. Pettigrew reviews the radiographs and your pet’s medical history to confirm candidacy for TPLO.</p>
      <p>6. <b>Deposit:</b> A $3,500 deposit secures Dr. Pettigrew’s travel and surgery date. This is refundable if canceled at least 5 days prior to the scheduled procedure.</p>
      <p>7. <b>Surgery Day:</b> Your pet is dropped off in the morning and surgery is performed the same day.</p>
      <p>8. <b>Discharge:</b> You’ll receive a post-surgery update and your pet will go home that evening.</p>
      <p><b>Post-Operative Care &amp; Follow-Up Two follow-up appointments will be scheduled:</b></p>
      <p>● 4 Weeks Post-Op: Evaluate healing, refill medications, and address any questions.</p>
      <p>● 8 Weeks Post-Op: Sedated radiographs will confirm proper healing of the surgical site and tibia.</p>
      <p>Dr. Pettigrew will stay in direct contact with you during your pet’s recovery using her custom mobile app, which allows for secure messaging and provides detailed post-operative instructions.</p>
    </div>
    <div class="specialist-panel">
      <p class="specialist-name">Helena<br>Pettigrew</p>
    </div>
    <p class="clinic-name clinic-name--back"><span class="mark"></span><span>Willow Crest Avenue Animal Clinic</span></p>
  </section>

  <section class="page page--front">
    <svg class="front-field" viewBox="0 0 560 793" preserveAspectRatio="none" aria-hidden="true">
      <polygon points="0,401 560,0 560,793 0,793" fill="var(--green)"/>
    </svg>
    <p class="clinic-name clinic-name--front"><span class="mark"></span><span>Willow Crest Avenue Animal Clinic</span></p>
    <p class="specialist-name specialist-name--front">Helena Pettigrew</p>

    <div class="photo-ring photo-ring--cat" role="img" aria-label="Photograph of an orange tabby cat sitting"></div>
    <div class="photo-ring photo-ring--pups" role="img" aria-label="Photograph of two golden retriever puppies on grass"></div>

    <div class="front-copy body-text">
      <p><b>Advanced Orthopedic Care by Dr. Helena Pettigrew, DVM, DACVS-sa</b></p>
      <p><b>TPLO Surgery at Willow Crest Avenue Animal Clinic</b></p>
      <p><b>About Dr. Helena Pettigrew:</b> Dr. Helena Pettigrew is a board-certified veterinary surgeon (Diplomate of the American College of Veterinary Surgeons) with over 18 years of experience in small animal surgery. A graduate of Northgrove State University, she completed her surgical residency at Ashby Hall School of Veterinary Medicine. Through her mobile practice, Fieldstone Surgical Services, Dr. Pettigrew now provides advanced surgical procedures—such as TPLO—directly at local clinics.</p>
      <p><b>What is TPLO Surgery?</b> Tibial Plateau Leveling Osteotomy (TPLO) is a surgical procedure that stabilizes the stifle (knee) joint following a cranial cruciate ligament (CCL) rupture—a common orthopedic injury in dogs. The procedure involves altering the angle of the tibial plateau to eliminate abnormal joint motion, restoring stability and improving function.</p>
      <p>Benefits of TPLO Surgery</p>
      <p>● <b>Enhanced Joint Stability:</b> Restores natural biomechanics, reducing pain and improving mobility.</p>
      <p>● <b>Faster Recovery:</b> Many dogs return to normal activity faster compared to other surgical techniques.</p>
      <p>● <b>Proven Long-Term Success:</b> TPLO is particularly effective in large and active breeds.</p>
      <p><b>Why Choose Willow Crest Avenue Animal Clinic?</b> Partnering with Dr. Pettigrew, Willow Crest Avenue Animal Clinic offers advanced orthopedic surgery on-site—eliminating the need for referrals or travel. This collaboration ensures your pet receives expert surgical care in a familiar, trusted environment.</p>
      <p>Our clinic works directly with your primary veterinarian to share medical records, diagnostics, and prescriptions, ensuring seamless and coordinated care for your pet.</p>
    </div>

    <div class="contacts">
      <div class="contact-block contact-block--clinic">
        <p class="contact-title">Willow Crest Avenue Animal Clinic</p>
        <p class="contact-line"><svg viewBox="0 0 10 10"><path d="M1 5 L5 1.5 L9 5 M2.5 4 V8.5 H7.5 V4" fill="none" stroke="var(--yellow)" stroke-width="1.3"/></svg><span>2280 Willow Crest Avenue, Brookferry, MI 48031</span></p>
        <p class="contact-line"><svg viewBox="0 0 10 10"><path d="M2 1 L4 1.2 L4.6 3.4 L3.4 4.3 Q4.5 6.2 5.7 6.6 L6.6 5.4 L8.8 6 L9 8 Q8 9.3 6.5 9 Q2.5 7.5 1 3.5 Q0.8 2 2 1 Z" fill="var(--yellow)"/></svg><span>(555) 318-2290</span></p>
        <p class="contact-line"><svg viewBox="0 0 10 10"><circle cx="5" cy="5" r="4" fill="none" stroke="var(--yellow)" stroke-width="1.2"/><path d="M1 5 H9 M5 1 Q2.6 5 5 9 M5 1 Q7.4 5 5 9" fill="none" stroke="var(--yellow)" stroke-width=".9"/></svg><span>info@brookferrypetcare.com</span></p>
      </div>
      <div class="contact-block contact-block--surgeon">
        <p class="contact-title">Fieldstone Surgical Services (Dr. Helena Pettigrew)</p>
        <p class="contact-line"><svg viewBox="0 0 10 10"><path d="M2 1 L4 1.2 L4.6 3.4 L3.4 4.3 Q4.5 6.2 5.7 6.6 L6.6 5.4 L8.8 6 L9 8 Q8 9.3 6.5 9 Q2.5 7.5 1 3.5 Q0.8 2 2 1 Z" fill="var(--yellow)"/></svg><span>(555) 210-4477</span></p>
        <p class="contact-line"><svg viewBox="0 0 10 10"><rect x="1" y="2.2" width="8" height="5.8" fill="none" stroke="var(--yellow)" stroke-width="1.1"/><path d="M1 2.4 L5 5.5 L9 2.4" fill="none" stroke="var(--yellow)" stroke-width="1.1"/></svg><span>drpettigrew@fieldstonesurgical.com</span></p>
        <p class="contact-line"><svg viewBox="0 0 10 10"><circle cx="5" cy="5" r="4" fill="none" stroke="var(--yellow)" stroke-width="1.2"/><path d="M1 5 H9 M5 1 Q2.6 5 5 9 M5 1 Q7.4 5 5 9" fill="none" stroke="var(--yellow)" stroke-width=".9"/></svg><span>www.northgroveanimalsurgery.com</span></p>
      </div>
    </div>
  </section>

</div>
</body>
</html>
```